Leading the way in online fitness and education requires power house web design

If you need to contact me you can do so via
skype: Travlin

We need a website designed for new company based in Houston Texas called "TravlinFit". We offer web based training and nutrition programs for our members for example we use the same software as these companies: http://marobelka.com/ http://www.liftquorra.com/ i would like my visitors to be captivated by the level of design creativity of the site.

colors to use would be grey, orange and green.
for example i like the green of this site http://www.cartbeam.com/
i will upload my logo files so you can get a feel for shades of grey and orange.

there is a 3d effect filter i would like applied to my logo for use in the web design i have uploaded what that effect looks like.

i will need your designs to be complete with all interior pages which will include Home, Fitness, Nutrition, Fit Lounge, Fit Score, Fit School, Contact Us, Sign up.

fit lounge on my site is the same as pathwick on liftquorra and locker room on marobelka just re branded.

fit school is a research corner for members to learn about health and fitness, we are members of major medical journals on health and fitness and will have all our articles be from the newest research findings.

competitor sites
these sites use same software:
http://marobelka.com/
http://www.liftquorra.com/

these sites are other software.
http://home.sprintmesa.com/software-for-athletes.aspx
http://www.vigordex.com/

here are some websites that i like:
http://www.crestwaveplay.com/
http://www.nub-lantern.com/
http://fimzol.com/
http://www.parqudo.com/
http://www.lortavi.de/fandiloop/
http://brisketmade.com/

i also like the greens in this site that i am uploading

I have been reviewing the designs and would like to update everyone at once I do not want a normal fitness website design style, no testimonials, blog post, bodyfat calculator

my website will be a membership based website. i want the website to sell the main points of my fitness app that my members will have access to look at the comments for my selling points, use those points in the site create designs and graphics to visualize those points.

look at these sites and gain inspiration

http://www.tuvelo.com.pl/#/projekty/case-studies
http://www.quendar.com/en#/home#ld-kpvm-402617-0045
http://www.nub-lantern.com/
http://fimzol.com/
http://www.parqudo.com/

i have a few designers asking me what the selling points are, the website needs to be built around these points

main selling points.

overview

programs utilize the best multi-joint exercises combined with high intensity cardio, to give you a full-body workout, efficiently and effectively. This means you’re burning more calories and building more lean muscle per unit of time than traditional weight training and cardio programs.

When you sign up, you''ll receive a work out and diet plan to fit your goals and fitness level. As you progress through your plan, you can use the personal fitness and meal calendar to record your results. When you sign-up we''ll ask you a series of questions and your workouts will be tailored to your exact needs. That means never having to use a generic diet and exercise plan again.

If you''ve ever tried to lose weight and build muscle and didn''t succeed, we feel your pain. Until now, trying to navigate all the fitness fads and latest trends on your own has been difficult. The best option - hiring a certified personal trainer - may be out of your financial reach. That''s where we come in - we''re personal trainers on a mission to help you reach your fitness goals quickly and for less money than in person training. Best of all, we''re here to help you day or night.

Fitness

Personal Fitness Calendar

Tailored to the member’s schedule and flexible to accommodate any changes to a member’s regular fitness schedule. Track your progress and stay on track with your fitness goals.

Custom Fitness Plan

Based on a member’s current physical condition and goals.

• Step by step exercise instructions
• 3-D video demonstrations of over 600 exercises, including functional and body-weight only movements
• Equipment filter can customize plans to your gym’s equipment package
• Record workouts to track exercise history and progression

Nutrition

Nutritional Assessment

Daily recommended caloric intake (Protein, Carbohydrates and Fats), based on personal profile and daily fitness plan.

Custom Meal Plan

Personalized meal plan based on nutritional assessment.

• Choose number of meals per day
• Add dietary restrictions, food preferences or dislikes
• Database of thousands of ingredients allows for hundreds of thousands of meal combinations
• Include favorite foods by entering custom nutritional information

Weight tracking

Calculate goal weight and track weight-loss or weight-gain progress. You will reach your goals in no time.

Fit Lounge

What is the most important part of any workout or fitness program? Staying motivated. And what better form of motivation than positive encouragement from your peers?

Fit Lounge is fitness focused social network for health-minded individuals looking for a simple and convenient place to track their workout goals and monitor their progress. A unique system of motivation, support and accountability makes setting fitness goals and then keeping up with them easy

Track

Start by setting fitness goals that you want to track. They can be anything from running and jogging to how many hours of sleep you are getting and how many glasses of water you are drinking every day. Other members of the travlinfits community might be tracking the same workout goals as you, so you can always join their groups as well.

Share

Once you start tracking your workout goals, you can share your progress with your friends. Reach a new max on your bench press? Let everyone know. Eclipse the 10 mile mark on your daily run? Spread the word! The communication of encouragement back and forth is a great way to ensure that everyone stays on track with their workout goals.

Achieve

Of course, the point of any workout or fitness program is to achieve the goals you’ve set. And with help from travlinfits workout tracking tools and encouragement from the community, you will achieve your workout goals in no time. When you see a friend has achieved his or her fitness goals, you can send them a virtual “fist bump” as a sign of congratulations. The number of “fist bumps” each user accumulates will be displayed on their profile, providing additional motivation and a healthy dose of competition.

Reason: i dont feel the designs i have received are of the quality i am looking for

check this website out, i know its flash, but i also know you can get creative without flash and have nice effects throughout the site.

http://www.driftlane-hub.com/

I dont want plain jane designs, insert the content i provided into the site and have it explored in a unique way. take as much time on the design as you need as i will keep extending deadline until i find one that is perfect.

as said before don't make the site anything like the competition sites, its only purpose is to sell the memberships using content provided so i need an innovative way to for them to explore that content,

as your designing this site add me on skype so i can detail and help brainstorm ideas my skype id is travlin
you can stray from the color scheme a little or throw it away if you want i just want to see how creative you can get.

Industry/Entity Type

School

Requirements
Nice to have
• if you notice at the bottom of http://marobelka.com/ she has the orange bar with the three short content parts, i like the idea of having a space like that for similar content.

on http://www.vigordex.com/ if you look to the left side of the scrolling icons i like the idea of having icons or animated pictures to point of key benefits.

```html
<!DOCTYPE html>
<html lang="en">
<head>
<meta charset="utf-8">
<title>TravlinFit – Your Personal Online Training Solution</title>
<link href="https://fonts.googleapis.com/css2?family=Exo:ital,wght@1,300&family=Noto+Sans:wght@400;700&family=PT+Sans:wght@400;700&family=PT+Sans+Narrow&display=swap" rel="stylesheet">
<style>
:root{
  --black:#050505;
  --header:#0b0b0b;
  --green:#3f9320;
  --green-dark:#2b6d12;
  --green-deep:#1d4a0b;
  --green-light:#67b52c;
  --orange:#f0661a;
  --orange-light:#ff8a2a;
  --white:#ffffff;
  --grey:#9a9a9a;
  --icon:#2a2a2a;
}
*{box-sizing:border-box;margin:0;padding:0}
html,body{width:1200px;height:1200px;overflow:hidden;background:var(--black)}
body{position:relative;font-family:"PT Sans",sans-serif;color:var(--white)}

.site-header{position:absolute;left:0;top:0;width:1200px;height:128px;background:var(--header)}
.site-header::before{content:"";position:absolute;left:130px;top:0;width:400px;height:128px;background:radial-gradient(ellipse at 50% 40%,#2a2a2a,transparent 70%)}
.brand{position:absolute;left:140px;top:42px;display:flex;align-items:center;gap:12px}
.brand-mark{width:44px;height:44px;border-radius:50%;background:var(--orange)}
.brand-name{font-family:"Noto Sans",sans-serif;font-weight:700;font-size:36px;color:var(--white)}
.brand-tagline{position:absolute;left:224px;top:92px;font-family:"Noto Sans",sans-serif;font-size:11px;font-weight:700;letter-spacing:.2px;color:#ddd}
.util-links{position:absolute;right:132px;top:6px;display:flex;gap:16px;font-size:12px;font-family:"Noto Sans",sans-serif}
.util-links span{display:flex;align-items:center;gap:5px}
.util-links i{display:inline-block;width:10px;height:11px;background:#fff;border-radius:2px}
.social{position:absolute;right:140px;top:58px;display:flex;gap:8px}
.social span{width:36px;height:36px;background:#3a5a95;border:1px solid #888;font-size:0}
.social span+span{background:#3fb3e0}

.hero{position:absolute;left:0;top:128px;width:1200px;height:468px;background:radial-gradient(ellipse at 55% 45%,var(--green-light),var(--green) 45%,var(--green-dark) 100%);border-top:2px solid #5c9a3a;overflow:hidden}
.hero-rings{position:absolute;left:430px;top:140px;width:420px;height:260px;border-radius:50%;border:2px solid rgba(0,0,0,.06);box-shadow:0 0 0 18px rgba(0,0,0,.03)}
.main-nav{position:absolute;left:129px;top:0;width:941px;height:79px;border:1px solid rgba(255,255,255,.15);border-top:none;background:rgba(0,0,0,.05)}
.nav-item{position:absolute;top:14px;width:84px;height:56px;border-radius:4px;background:rgba(255,255,255,.06);border:1px solid rgba(0,0,0,.08);display:flex;align-items:center;justify-content:center}
.nav-item.home{background:linear-gradient(#8fd43a,#4ea81e);border:1px solid #9ee04f;flex-direction:column;justify-content:flex-end;padding-bottom:4px;font-family:"Noto Sans",sans-serif;font-weight:700;font-size:12px}
.nav-item.home svg{position:absolute;top:-10px;left:20px}
.hero-copy{position:absolute;left:156px;top:100px}
.welcome{font-family:"Exo",sans-serif;font-style:italic;font-weight:300;font-size:28px;color:#1d3a0e}
.headline{font-family:"Noto Sans",sans-serif;font-weight:700;font-size:60px;line-height:72px;letter-spacing:1px;margin-top:2px}
.hero-text{font-size:16px;line-height:20px;width:490px;margin-top:12px}
.hero-text+.hero-text{margin-top:9px}
.cta{position:absolute;left:146px;top:382px;width:442px;height:70px;display:flex}
.cta-note{width:262px;background:linear-gradient(#2a2a2a,#0a0a0a);border-radius:6px 0 0 6px;padding:12px 17px}
.cta-note strong{display:block;font-family:"Noto Sans",sans-serif;font-size:17px}
.cta-note em{font-style:normal;color:var(--orange-light);font-size:15px}
.cta-button{flex:1;background:linear-gradient(var(--orange-light),var(--orange));clip-path:polygon(0 0,100% 0,78% 100%,0 100%);font-family:"Noto Sans",sans-serif;font-weight:700;font-size:17px;padding:23px 0 0 16px;letter-spacing:.5px}
.hero-photo{position:absolute;left:690px;top:-14px;width:320px;height:482px;background:linear-gradient(160deg,#c8926c,#9b6a4a 60%,#5b5b5b);border-radius:140px 140px 0 0}

.features{position:absolute;left:0;top:598px;width:1200px;height:462px;background:radial-gradient(ellipse at center,var(--green),var(--green-dark))}
.features-frame{position:absolute;left:129px;top:0;width:943px;height:458px;border:1px solid rgba(0,0,0,.2);border-top:none;background:rgba(0,0,0,.06)}
.card{position:absolute;width:431px;height:171px;background:linear-gradient(90deg,var(--green-dark),#4f9a22);border:1px solid rgba(255,255,255,.12);box-shadow:0 2px 6px rgba(0,0,0,.35);overflow:hidden}
.card h2{position:absolute;left:21px;top:17px;font-family:"Noto Sans",sans-serif;font-size:19px;line-height:25px;font-weight:700}
.card p{position:absolute;left:21px;font-size:12.5px;line-height:16px}
.card .photo{position:absolute;right:0;top:0;height:100%;background:linear-gradient(90deg,#b88566,#8e5f40)}
.read-more{position:absolute;left:20px;bottom:12px;width:134px;height:36px;display:flex}
.read-more .go{width:40px;background:#111;border-radius:4px 0 0 4px;display:flex;align-items:center;justify-content:center}
.read-more .label{flex:1;background:linear-gradient(var(--orange-light),var(--orange));clip-path:polygon(0 0,100% 0,70% 100%,0 100%);font-family:"Noto Sans",sans-serif;font-weight:700;font-size:10px;padding:12px 0 0 12px}

.footer-nav{position:absolute;left:0;top:1060px;width:1200px;height:48px;background:var(--green-deep);border-top:1px solid #3a6d22;display:flex;align-items:center;padding-left:145px;font-family:"PT Sans Narrow",sans-serif;font-size:15px}
.footer-nav span+span::before{content:"I";margin:0 15px;font-size:12px}
.legal{position:absolute;left:0;top:1108px;width:1200px;height:92px;background:var(--black)}
.copyright{position:absolute;left:145px;top:18px;color:var(--grey);font-size:14px}
.legal-links{position:absolute;right:154px;top:17px;color:var(--grey);font-family:"PT Sans Narrow",sans-serif;font-size:13px}
.legal-links span+span::before{content:"I";margin:0 12px}
</style>
</head>
<body>

<header class="site-header">
  <div class="brand"><span class="brand-mark"></span><span class="brand-name">TravlinFit</span></div>
  <div class="brand-tagline">YOUR PERSONAL ONLINE TRAINING SOLUTION</div>
  <nav class="util-links">
    <span><i></i>Bookmark</span><span><i></i>Contact</span><span><i></i>Register</span><span><i></i>Login</span>
  </nav>
  <div class="social"><span>Friendloop</span><span>Chirpline</span></div>
</header>

<section class="hero">
  <div class="hero-rings"></div>
  <nav class="main-nav">
    <div class="nav-item home" style="left:27px">
      <svg width="44" height="42" viewBox="0 0 44 42"><polygon points="22,2 42,20 36,20 36,40 8,40 8,20 2,20" fill="#f2f2f2" stroke="#555" stroke-width="1.5"/><rect x="18" y="26" width="8" height="14" fill="#6b8fb5"/></svg>
      HOME
    </div>
    <div class="nav-item" style="left:117px"><svg width="60" height="50"><circle cx="30" cy="28" r="13" fill="var(--icon)"/><rect x="24" y="10" width="12" height="6" rx="3" fill="none" stroke="var(--icon)" stroke-width="4"/><rect x="4" y="34" width="52" height="4" fill="var(--icon)"/><rect x="8" y="28" width="4" height="16" fill="var(--icon)"/></svg></div>
    <div class="nav-item" style="left:207px"><svg width="50" height="50"><circle cx="25" cy="29" r="17" fill="var(--icon)"/><rect x="24" y="6" width="4" height="10" fill="var(--icon)"/></svg></div>
    <div class="nav-item" style="left:297px"><svg width="50" height="50"><circle cx="25" cy="28" r="18" fill="var(--icon)"/><rect x="21" y="4" width="8" height="6" fill="var(--icon)"/></svg></div>
    <div class="nav-item" style="left:387px"><svg width="54" height="50"><path d="M5 12 H49 Q46 42 27 42 Q8 42 5 12Z" fill="var(--icon)"/></svg></div>
    <div class="nav-item" style="left:477px"><svg width="54" height="50"><path d="M6 8 H48 V36 H20 L12 44 V36 H6Z" fill="var(--icon)"/></svg></div>
    <div class="nav-item" style="left:567px"><svg width="60" height="50"><rect x="4" y="8" width="52" height="32" fill="var(--icon)" stroke="#555"/></svg></div>
    <div class="nav-item" style="left:831px"><svg width="50" height="50"><circle cx="25" cy="25" r="20" fill="var(--icon)"/></svg></div>
  </nav>

  <div class="hero-copy">
    <p class="welcome">Welcome to TravlinFit:</p>
    <h1 class="headline">REACH YOUR<br>GOALS QUICKLY.</h1>
    <p class="hero-text">We're personal trainers on a mission to help you reach your fitness goals quickly and for less money.</p>
    <p class="hero-text">Best of all, we're here to help you day or night.</p>
  </div>

  <div class="cta">
    <div class="cta-note"><strong>Be your own success story.</strong><em>Get started today</em></div>
    <div class="cta-button">SIGN UP NOW</div>
  </div>

  <div class="hero-photo" role="img" aria-label="Photo of a smiling athletic man holding a dumbbell toward the viewer"></div>
</section>

<section class="features">
  <div class="features-frame"></div>

  <article class="card" style="left:157px;top:29px">
    <div class="photo" role="img" aria-label="Photo of a man's and a woman's toned torsos" style="width:240px"></div>
    <h2>Serious about<br>getting fit?</h2>
    <p style="top:80px">Sick of diets that don't work?<br>Want to build muscle?</p>
    <div class="read-more"><span class="go"><svg width="18" height="18"><polygon points="2,1 17,9 2,17" fill="#7cc242"/></svg></span><span class="label">Read More</span></div>
  </article>

  <article class="card" style="left:613px;top:29px">
    <div class="photo" role="img" aria-label="Photo of a smiling muscular man with a jump rope" style="width:200px"></div>
    <h2>Choose how and where<br>you workout.</h2>
    <p style="top:78px">You're not restricted to specific workout<br>plans and locations.</p>
    <div class="read-more"><span class="go"><svg width="18" height="18"><polygon points="2,1 17,9 2,17" fill="#7cc242"/></svg></span><span class="label">Read More</span></div>
  </article>

  <article class="card" style="left:157px;top:229px">
    <div class="photo" role="img" aria-label="Photo of a smiling woman holding a green apple" style="width:160px"></div>
    <h2>Eat right with meal plans<br>designed just for you.</h2>
    <p style="top:76px">Everything from your shopping list to your<br>meal plan and recipes are provided.</p>
    <div class="read-more"><span class="go"><svg width="18" height="18"><polygon points="2,1 17,9 2,17" fill="#7cc242"/></svg></span><span class="label">Read More</span></div>
  </article>

  <article class="card" style="left:613px;top:229px">
    <div class="photo" role="img" aria-label="Photo of a fit man and woman side by side" style="width:216px"></div>
    <h2>Achieve &amp; Share.</h2>
    <p style="top:61px">With your personal trainer by<br>your side your goals are achievable.</p>
    <div class="read-more"><span class="go"><svg width="18" height="18"><polygon points="2,1 17,9 2,17" fill="#7cc242"/></svg></span><span class="label">Read More</span></div>
  </article>
</section>

<nav class="footer-nav">
  <span>HOME</span><span>FITNESS</span><span>NUTTRITION</span><span>FIT SCORE</span><span>FIT LOUNGE</span><span>FIT SCHOOL</span><span>SIGNU UP</span><span>LOGIN</span><span>CONTACT</span><span>ABOUT TRAVLINFIT</span>
</nav>

<footer class="legal">
  <p class="copyright">© 2012 All Rights Reserved. TravlinFit</p>
  <p class="legal-links"><span>SITEMAP</span><span>TERMS &amp; CONDITIONS</span><span>PRIVACY POLICY</span></p>
</footer>

</body>
</html>
```